Technology Solutions Provider

Let’s design a business card that will be as simple and bold at the same time. Name, email address, website & phone number.

Target Market(s)

Small to Medium Size Business

Industry/Entity Type

It Professional

Contact Information for Business Card

Name, email, website, phone numbers

Font styles to use
Sans Serif

Colors
ec1f27
f04a50
dddddd
919191
000000
ffffff

Requirements
Must have
• Clean simple look using my existing logo. I just need to the basic contact information on this card.
Nice to have
• Im considering the square size card versus the standard size business card.
Should not have
• No Mailing Address, no list of services.

```html
<!DOCTYPE html>
<html lang="en">
<head>
<meta charset="utf-8">
<title>Vantora – Business Card</title>
<link href="https://fonts.googleapis.com/css2?family=Exo+2:wght@700;800&family=Crimson+Text&family=Open+Sans:wght@400&display=swap" rel="stylesheet">
<style>
  :root {
    --brand-red: #ec1f27;
    --ink: #231f20;
    --ink-soft: #302c2d;
    --paper: #f2f2f2;
    --muted: #919191;
    --white: #ffffff;
    --backdrop: #3a3a3a;
  }
  * { margin: 0; padding: 0; box-sizing: border-box; }
  html, body { width: 1200px; height: 751px; overflow: hidden; }
  body { background: var(--backdrop); position: relative; }

  .card {
    position: absolute;
    width: 343px; height: 343px;
    transform: scale(0.9388);
    transform-origin: 0 0;
    overflow: hidden;
  }
  .card--front { left: 224px; top: 213px; background: var(--paper); }
  .card--back  { left: 615px; top: 213px; background: var(--ink-soft); }

  .card__band {
    position: absolute;
    left: 0; right: 0; bottom: 0;
    height: 115px;
    background: var(--brand-red);
  }

  .brand { position: absolute; left: 41px; top: 44px; }
  .brand__name {
    font-family: "Exo 2", sans-serif;
    font-weight: 700;
    font-size: 30px;
    line-height: 1;
    color: var(--brand-red);
    letter-spacing: 0.5px;
  }
  .brand__tagline {
    font-family: "Crimson Text", serif;
    font-size: 11px;
    color: var(--muted);
    margin-top: 2px;
  }

  .person { position: absolute; left: 43px; top: 121px; }
  .person__name {
    font-family: "Exo 2", sans-serif;
    font-weight: 800;
    font-size: 19px;
    color: var(--brand-red);
    letter-spacing: 0.3px;
  }
  .person__role {
    font-family: "Exo 2", sans-serif;
    font-weight: 700;
    font-size: 13px;
    color: var(--ink);
    margin-top: 2px;
    letter-spacing: 0.3px;
  }

  .contacts {
    position: absolute;
    right: 16px; top: 254px;
    list-style: none;
    font-family: "Crimson Text", serif;
    font-size: 15px;
    line-height: 19px;
    color: var(--white);
    text-align: right;
  }
  .contacts li { display: flex; justify-content: flex-end; align-items: center; gap: 8px; }
  .contacts svg { width: 13px; height: 13px; flex: none; }

  .back__name {
    position: absolute; left: 0; right: 0; top: 140px;
    text-align: center;
    font-family: "Exo 2", sans-serif;
    font-weight: 700;
    font-size: 40px;
    color: var(--white);
  }
  .back__url {
    position: absolute; left: 0; right: 0; top: 290px;
    text-align: center;
    font-family: "Open Sans", sans-serif;
    font-size: 13px;
    letter-spacing: 5px;
    color: var(--white);
  }
</style>
</head>
<body>
  <section class="card card--front">
    <div class="card__band"></div>

    <div class="brand">
      <div class="brand__name">vantora</div>
      <div class="brand__tagline">technology solutions provider</div>
    </div>

    <div class="person">
      <div class="person__name">DANIEL REYES</div>
      <div class="person__role">CEO/FOUNDER</div>
    </div>

    <ul class="contacts">
      <li>415 302 7781
        <svg viewBox="0 0 14 14" aria-hidden="true"><path fill="#fff" d="M1,5 C1,2 13,2 13,5 L13,6 L10,6 L10,5 L4,5 L4,6 L1,6 Z M3,7 L11,7 L12,13 L2,13 Z"/><circle cx="7" cy="10" r="1.6" fill="var(--brand-red)"/></svg>
      </li>
      <li>415 908 2264
        <svg viewBox="0 0 14 14" aria-hidden="true"><rect x="3.5" y="0.5" width="7" height="13" rx="1.2" fill="#fff"/><rect x="5" y="2" width="4" height="8.5" fill="var(--brand-red)"/></svg>
      </li>
      <li>daniel@vantora.net
        <svg viewBox="0 0 14 14" aria-hidden="true"><rect x="1" y="3.5" width="12" height="8" fill="#fff"/><path d="M1,3.5 L7,8 L13,3.5" fill="none" stroke="var(--brand-red)" stroke-width="1"/></svg>
      </li>
      <li>www.vantora.net
        <svg viewBox="0 0 14 14" aria-hidden="true"><circle cx="7" cy="7" r="6" fill="#fff"/><path d="M1,7 L13,7 M7,1 C4,4 4,10 7,13 C10,10 10,4 7,1" fill="none" stroke="var(--brand-red)" stroke-width="1"/></svg>
      </li>
    </ul>
  </section>

  <section class="card card--back">
    <div class="back__name">vantora</div>
    <div class="back__url">www.vantora.net</div>
  </section>
</body>
</html>
```